Now Leasing Banner

Looking for a banner that says the following information approx 4' x 30'

Now Leasing Maplewood Terrace 925-318-6054

Target Market(s)

Drive by traffic

Industry/Entity Type

Residential property management

Requirements
Must have
• Clear and readable from a distance

```html
<!DOCTYPE html>
<html lang="en">
<head>
<meta charset="utf-8">
<title>Now Leasing Banner – Maplewood Terrace</title>
<link rel="stylesheet" href="https://fonts.googleapis.com/css2?family=Yellowtail&family=Playfair+Display:wght@700&family=Cormorant+Garamond:ital,wght@1,600&family=Arimo:wght@700&display=swap">
<style>
  :root {
    --backdrop: #e0e1df;
    --sage: #94ab54;
    --charcoal: #282828;
    --cream: #f9f5e0;
    --white: #ffffff;
  }
  * { margin: 0; padding: 0; box-sizing: border-box; }
  html, body {
    width: 1200px;
    height: 469px;
    overflow: hidden;
    background: var(--backdrop);
  }
  .canvas {
    position: relative;
    width: 1200px;
    height: 469px;
  }
  .banner {
    position: absolute;
    left: 41px;
    width: 1118px;
    height: 149px;
    overflow: hidden;
  }
  .banner--dark { top: 55px; background: var(--charcoal); }
  .banner--light { top: 254px; background: var(--sage); }
  .banner__panel {
    position: absolute;
    inset: 0;
    width: 100%;
    height: 100%;
  }
  .headline {
    position: absolute;
    left: 28px;
    top: 0;
    height: 149px;
    display: flex;
    align-items: baseline;
    white-space: nowrap;
    padding-top: 8px;
  }
  .headline__now {
    font-family: "Yellowtail", cursive;
    font-size: 74px;
    line-height: 1;
    color: var(--charcoal);
    margin-right: 8px;
  }
  .headline__leasing {
    font-family: "Playfair Display", serif;
    font-weight: 700;
    font-size: 104px;
    line-height: 1.18;
    letter-spacing: 0;
  }
  .banner--dark .headline__leasing { color: var(--cream); }
  .banner--light .headline__leasing { color: var(--sage); }
  .contact {
    position: absolute;
    left: 734px;
    top: 22px;
    color: var(--white);
  }
  .contact__name {
    font-family: "Cormorant Garamond", serif;
    font-style: italic;
    font-weight: 600;
    font-size: 44px;
    line-height: 1;
    white-space: nowrap;
  }
  .contact__phone {
    font-family: "Arimo", sans-serif;
    font-weight: 700;
    font-size: 35px;
    line-height: 1;
    margin-top: 22px;
    letter-spacing: 0.5px;
  }
</style>
</head>
<body>
<main class="canvas">
  <section class="banner banner--dark">
    <svg class="banner__panel" viewBox="0 0 2159 287" preserveAspectRatio="none" aria-hidden="true">
      <path d="M0 0 H1300 C1345 0 1366 40 1366 75 C1366 92 1361 104 1355 115 L1266 287 H0 Z" fill="var(--sage)"/>
    </svg>
    <h1 class="headline"><span class="headline__now">Now</span><span class="headline__leasing">LEASING</span></h1>
    <div class="contact">
      <p class="contact__name">Maplewood Terrace</p>
      <p class="contact__phone">925-318-6054</p>
    </div>
  </section>

  <section class="banner banner--light">
    <svg class="banner__panel" viewBox="0 0 2159 287" preserveAspectRatio="none" aria-hidden="true">
      <path d="M0 0 H1250 C1310 0 1348 50 1348 100 C1348 122 1342 138 1335 152 L1266 287 H0 Z" fill="var(--cream)"/>
    </svg>
    <h2 class="headline"><span class="headline__now">Now</span><span class="headline__leasing">LEASING</span></h2>
    <div class="contact">
      <p class="contact__name">Maplewood Terrace</p>
      <p class="contact__phone">925-318-6054</p>
    </div>
  </section>
</main>
</body>
</html>
```